Global Nano Technology Surface Protection company needs a new logo and cards

We are a Global company that will apply nanotechnology coatings on surfaces to prevent growth and spread of bacteria, viruses, mold etc. We deal with large corporates, airlines, hospitals and schools so we are after a new modern, simple and clean look that will have great visual impact.
We a company that is focused on prevention and protection.

Company name, Quorvane Systems Worldwide

Subtext, Antimicrobial Surface Protection

Logo, QVSW or QSW

Target Market(s)

Hospitals, Transport agencies, Airlines, Corporate entities

Industry/Entity Type

Protection

Contact Information for Business Card

Logo, QVSW or QSW
www.qvsw-example.us
Derek Holloway
+64290536218
tidyshieldnz@mailbox-example.com

Logo Text

QVSW

Requirements
Must have
• Simple clean look
Should not have
• Nothing too messy

```html
<!DOCTYPE html>
<html lang="en">
<head>
<meta charset="utf-8">
<title>Quorvane Systems Worldwide – Business Card</title>
<link href="https://fonts.googleapis.com/css2?family=Figtree:wght@400;500;700&family=Lato:wght@400&display=swap" rel="stylesheet">
<style>
  :root {
    --backdrop: #1a1a1a;
    --card-dark: #0d0d0d;
    --panel-light: #2e2e2e;
    --panel-dark: #141414;
    --logo-grey: #8f8f8f;
    --url-grey: #6e6e6e;
    --card-light-top: #ffffff;
    --card-light-bottom: #d9d9d9;
    --ink: #2b2b2b;
  }
  * { margin: 0; padding: 0; box-sizing: border-box; }
  html, body { width: 1200px; height: 900px; overflow: hidden; }
  body { background: var(--backdrop); position: relative; font-family: "Figtree", sans-serif; }

  .card { position: absolute; left: 308px; width: 616px; height: 352px; }

  .card-front { top: 64px; background: var(--card-dark); }
  .front-panel {
    position: absolute; left: 10px; top: 10px; width: 340px; height: 332px;
    background: linear-gradient(135deg, var(--panel-light) 0%, var(--panel-dark) 100%);
  }
  .brand-mark {
    position: absolute; left: 400px; top: 136px; width: 168px;
    display: flex; align-items: center; justify-content: center; gap: 10px;
  }
  .brand-square { width: 16px; height: 16px; background: var(--logo-grey); }
  .brand-name { font-weight: 700; font-size: 46px; color: var(--logo-grey); letter-spacing: -1px; line-height: 1; }
  .front-url {
    position: absolute; left: 360px; top: 234px; width: 248px; text-align: center;
    font-family: "Lato", sans-serif; font-size: 18px; color: var(--url-grey);
  }

  .card-back {
    top: 440px;
    background: linear-gradient(160deg, var(--card-light-top) 0%, var(--card-light-bottom) 100%);
    color: var(--ink); text-align: center;
  }
  .back-line { position: absolute; left: 0; width: 100%; }
  .person-name { top: 69px; font-size: 28px; font-weight: 700; letter-spacing: 0.5px; }
  .person-title { top: 104px; font-size: 14px; font-weight: 500; letter-spacing: 0.5px; }
  .divider { top: 137px; left: 302px; width: 12px; height: 1.5px; background: var(--ink); }
  .company-name { top: 154px; font-size: 14.5px; font-weight: 500; letter-spacing: 0.3px; }
  .company-tagline { top: 180px; font-size: 14.5px; font-weight: 500; letter-spacing: 0.3px; }
  .contact-icons { top: 209px; display: flex; justify-content: center; gap: 12px; }
  .contact-icons svg { width: 16px; height: 16px; }
  .contact-phone { top: 235px; font-size: 14px; }
  .contact-email { top: 258px; font-size: 14px; }
  .contact-web { top: 281px; font-size: 14px; font-weight: 500; }
</style>
</head>
<body>
  <section class="card card-front">
    <div class="front-panel" role="img" aria-label="Decorative diagonal line pattern area in dark greys"></div>
    <div class="brand-mark">
      <span class="brand-square"></span>
      <span class="brand-name">QVSW</span>
    </div>
    <div class="front-url">www.qvsw-example.us</div>
  </section>

  <section class="card card-back">
    <div class="back-line person-name">DEREK HOLLOWAY</div>
    <div class="back-line person-title">Managing Director</div>
    <div class="back-line divider"></div>
    <div class="back-line company-name">Quorvane Systems Worldwide</div>
    <div class="back-line company-tagline">Antimicrobial Surface Protection</div>
    <div class="back-line contact-icons">
      <svg viewBox="0 0 16 16" aria-label="Phone">
        <circle cx="8" cy="8" r="8" fill="var(--ink)"/>
        <path d="M5 6.5h6l-1 4H6z M4.5 5.5q3.5-2 7 0v1h-7z" fill="#fff"/>
      </svg>
      <svg viewBox="0 0 16 16" aria-label="Email">
        <circle cx="8" cy="8" r="8" fill="var(--ink)"/>
        <rect x="4.3" y="5.3" width="7.4" height="5.4" fill="none" stroke="#fff" stroke-width="1"/>
        <path d="M4.3 5.3L8 8.4l3.7-3.1" fill="none" stroke="#fff" stroke-width="1"/>
      </svg>
      <svg viewBox="0 0 16 16" aria-label="Website">
        <circle cx="8" cy="8" r="8" fill="var(--ink)"/>
        <path d="M7 9l2-2 M6.8 7.2l-1.3 1.3a1.5 1.5 0 0 0 2 2l1.3-1.3 M9.2 8.8l1.3-1.3a1.5 1.5 0 0 0-2-2L7.2 6.8" fill="none" stroke="#fff" stroke-width="1" stroke-linecap="round"/>
      </svg>
    </div>
    <div class="back-line contact-phone">+64 290 536 218</div>
    <div class="back-line contact-email">tidyshieldnz@mailbox-example.com</div>
    <div class="back-line contact-web">www.qvsw-example.us</div>
  </section>
</body>
</html>
```